Emotional Historical Fiction Book Cover Design

The novel is about the Velmarsk incident. I interviewed several people with first-hand accounts, and it's an emotional event. I'd like to have it published, but will need a cover for it.

The story follows the path of 3 characters, a child, a young woman and an elderly man. The theme of memory and nostalgia flow through each, as well as the feeling of being uprooted.

The title is "the hush of rain" and is metaphorical to the story. I imagine the design will be as simplistic as possible.

Target Market(s)

teen - adult; 18+

Industry/Entity Type

Event

Colors

Designer to choose colors to be used in the design.

Requirements
Must have
• the title: the hush of rain (in all lower case)
• the author: Norah Pelligrave
• Somewhere "a novel" must be written

```html
<!DOCTYPE html>
<html lang="en">
<head>
<meta charset="utf-8">
<title>the hush of rain — Norah Pelligrave</title>
<link rel="stylesheet" href="https://fonts.googleapis.com/css2?family=Barlow+Condensed:wght@600;700&family=Barlow+Semi+Condensed:wght@600&display=swap">
<style>
  :root {
    --backdrop: #dcdcdc;
    --ink: #0d0a08;
    --sky-light: #f6ddcc;
    --sky-mid: #e9a27c;
    --rust: #b5532a;
    --rust-deep: #5a2210;
  }
  html, body {
    margin: 0;
    padding: 0;
    width: 1200px;
    height: 1200px;
    overflow: hidden;
    background: var(--backdrop);
  }
  .book-cover {
    position: absolute;
    left: 280px;
    top: 120px;
    width: 640px;
    height: 960px;
    overflow: hidden;
    box-shadow: 0 18px 40px rgba(0,0,0,0.18);
  }
  .cover-photo {
    position: absolute;
    inset: 0;
    background:
      linear-gradient(100deg, rgba(120,45,18,0.75) 0%, rgba(120,45,18,0.35) 38%, rgba(120,45,18,0) 55%),
      linear-gradient(180deg, var(--sky-mid) 0%, var(--sky-light) 45%, var(--sky-light) 58%, var(--rust) 70%, var(--rust-deep) 100%);
  }
  .author {
    position: absolute;
    left: 258px;
    top: 36px;
    margin: 0;
    font-family: "Barlow Condensed", sans-serif;
    font-weight: 700;
    font-size: 27px;
    letter-spacing: 0.5px;
    text-transform: uppercase;
    color: var(--ink);
  }
  .title {
    margin: 0;
    font-family: "Barlow Semi Condensed", sans-serif;
    font-weight: 600;
    color: var(--ink);
    line-height: 1;
  }
  .title-word {
    position: absolute;
    display: block;
    letter-spacing: -2px;
  }
  .title-the  { left: 252px; top: 112px; font-size: 132px; }
  .title-hush { left: 330px; top: 212px; font-size: 112px; }
  .title-of   { left: 240px; top: 318px; font-size: 78px; }
  .title-rain { left: 300px; top: 338px; font-size: 156px; }
  .tagline {
    position: absolute;
    left: 348px;
    top: 556px;
    margin: 0;
    font-family: "Barlow Condensed", sans-serif;
    font-weight: 700;
    font-size: 32px;
    text-transform: uppercase;
    color: var(--ink);
  }
</style>
</head>
<body>
  <div class="book-cover">
    <div class="cover-photo" role="img" aria-label="Rust-toned photograph of an abandoned power plant with tall lattice-framed ventilation stacks against a cloudy sky"></div>
    <p class="author">Norah Pelligrave</p>
    <h1 class="title">
      <span class="title-word title-the">the</span>
      <span class="title-word title-hush">hush</span>
      <span class="title-word title-of">of</span>
      <span class="title-word title-rain">rain</span>
    </h1>
    <p class="tagline">A Novel</p>
  </div>
</body>
</html>
```